Tradeline Summit & Expo xmas banner/MREC promotion

Size:
• Leader board: 728 x 90 px
• MREC: 300 x250 px
• Half-page: 300 x 600
• Wide skyscraper: 160 x 600
Image:
Candy cane stripes as the background – image bought. Horizontal or vertical whatever you think will works.
White strip/background for the copy? See images example – unless you don’t need to do that?
Bold font which is "neutra" to our other banners attached. I think black font would look good.
Message:
Please give it a good readable pace between slides – 3 secs?
1st Slide
It’s silly season!
2nd Slide
Treat yourself to an end of year gift
3rd Slide
Book your ticket now and save $$$
4th Slide
Get spoilt. You’re worth it!
5th Slide
Tradeline logo
Target Market(s)
anyone that sells online
• Automotive • Advertising • Digital • Entertainment
• Finance • Hospitality • Pharmaceutical/Healthcare • Pop Culture
• Retail • Travel • Telecommunications

```html
<!DOCTYPE html>
<html lang="en">
<head>
<meta charset="utf-8">
<title>Silly Season Banner Set</title>
<link rel="stylesheet" href="https://fonts.googleapis.com/css2?family=Outfit:wght@700&family=Ubuntu:wght@500&display=swap">
<style>
  :root {
    --page-bg: #f2f2f2;
    --page-bg-dot: #e9e9e9;
    --candy-red: #d3141c;
    --candy-red-deep: #a80d12;
    --candy-cream: #f1e6e0;
    --strip-light: #fbfbfb;
    --strip-shade: #e3e3e3;
    --headline-red: #c10e17;
    --note-grey: #707070;
  }
  html, body {
    margin: 0;
    padding: 0;
    overflow: hidden;
  }
  body {
    width: 1200px;
    height: 980px;
    position: relative;
    background-color: var(--page-bg);
    background-image: radial-gradient(var(--page-bg-dot) 1px, transparent 1px);
    background-size: 4px 4px;
    font-family: "Outfit", sans-serif;
  }
  .banner {
    position: absolute;
    overflow: hidden;
    box-shadow: 0 0 0 1px rgba(0,0,0,0.04);
  }
  .banner__photo {
    position: absolute;
    inset: 0;
    background: linear-gradient(155deg, var(--candy-red) 0%, var(--candy-cream) 30%, var(--candy-red) 50%, var(--candy-cream) 72%, var(--candy-red-deep) 100%);
  }
  .banner__strip {
    position: absolute;
    inset: 0;
    width: 100%;
    height: 100%;
  }
  .banner__headline {
    position: absolute;
    left: 0;
    right: 0;
    margin: 0;
    text-align: center;
    color: var(--headline-red);
    font-weight: 700;
    text-transform: uppercase;
    letter-spacing: 0.01em;
    line-height: 1.05;
    white-space: nowrap;
    transform: translateY(-50%);
  }
  .banner--leaderboard { left: 72px; top: 19px; width: 972px; height: 120px; }
  .banner--leaderboard .banner__headline { top: 58px; font-size: 41px; }
  .banner--half-page { left: 72px; top: 159px; width: 401px; height: 802px; }
  .banner--half-page .banner__headline { top: 400px; font-size: 37px; }
  .banner--skyscraper { left: 493px; top: 159px; width: 214px; height: 802px; }
  .banner--skyscraper .banner__headline { top: 400px; font-size: 30px; }
  .banner--mrec { left: 727px; top: 159px; width: 401px; height: 334px; }
  .banner--mrec .banner__headline { top: 167px; font-size: 35px; }
  .animation-note {
    position: absolute;
    left: 697px;
    top: 508px;
    width: 461px;
    margin: 0;
    text-align: center;
    color: var(--note-grey);
    font-family: "Ubuntu", sans-serif;
    font-weight: 500;
    font-size: 33px;
    line-height: 48px;
    text-transform: uppercase;
    white-space: nowrap;
  }
</style>
</head>
<body>
  <svg width="0" height="0" style="position:absolute" aria-hidden="true">
    <defs>
      <linearGradient id="strip-fill" x1="0" y1="0" x2="0" y2="1">
        <stop offset="0" stop-color="var(--strip-shade)"/>
        <stop offset="0.3" stop-color="var(--strip-light)"/>
        <stop offset="0.7" stop-color="var(--strip-light)"/>
        <stop offset="1" stop-color="var(--strip-shade)"/>
      </linearGradient>
    </defs>
  </svg>

  <section class="banner banner--leaderboard" aria-label="Leaderboard 728 by 90">
    <div class="banner__photo" role="img" aria-label="Close-up photo of red and white candy cane stripes"></div>
    <svg class="banner__strip" viewBox="0 0 972 120" preserveAspectRatio="none" aria-hidden="true">
      <path d="M226,0 L746,0 Q722,60 746,120 L226,120 Q250,60 226,0 Z" fill="url(#strip-fill)"/>
    </svg>
    <p class="banner__headline">It’s silly season!</p>
  </section>

  <section class="banner banner--half-page" aria-label="Half-page 300 by 600">
    <div class="banner__photo" role="img" aria-label="Close-up photo of red and white candy cane stripes"></div>
    <svg class="banner__strip" viewBox="0 0 401 802" preserveAspectRatio="none" aria-hidden="true">
      <path d="M0,330 Q200,350 401,330 L401,460 Q200,436 0,460 Z" fill="url(#strip-fill)"/>
    </svg>
    <p class="banner__headline">It’s silly season!</p>
  </section>

  <section class="banner banner--skyscraper" aria-label="Wide skyscraper 160 by 600">
    <div class="banner__photo" role="img" aria-label="Close-up photo of red and white candy cane stripes"></div>
    <svg class="banner__strip" viewBox="0 0 214 802" preserveAspectRatio="none" aria-hidden="true">
      <path d="M0,272 Q107,345 214,272 L214,518 Q107,476 0,518 Z" fill="url(#strip-fill)"/>
    </svg>
    <p class="banner__headline">It’s silly<br>season!</p>
  </section>

  <section class="banner banner--mrec" aria-label="MREC 300 by 250">
    <div class="banner__photo" role="img" aria-label="Close-up photo of red and white candy cane stripes"></div>
    <svg class="banner__strip" viewBox="0 0 401 334" preserveAspectRatio="none" aria-hidden="true">
      <path d="M0,113 Q200,128 401,113 L401,230 Q200,216 0,230 Z" fill="url(#strip-fill)"/>
    </svg>
    <p class="banner__headline">It’s silly season!</p>
  </section>

  <p class="animation-note">See the links<br>in the description<br>to see the animation</p>
</body>
</html>
```